Bubble solution bottle label for children

I would like a design for a label for a new bubble solution we have created. We'd like it to appeal to parents as well as 5-10 year old kids. It needs to be whimsical and attractive. The name of the bubbles is:

Floaty Pops!

We also need a portion of the label to include the following warning:
"Do not drink bubble solution. If swallowed drink lots of water. Bubble solution is not intended for human or animal consumption. If it comes in contact with your eyes, rinse immediately with water"

The label is full bleed and needs to meet the criteria below:
Horizontal
3.54" x 2.05"
90 x 52 mm
1063 x 615 pixels

Target Market(s)

5-10 years old children and their parents

Font styles to use
Serif
Script

Requirements
Must have
• Warning label as written in description. Must be whimsical and attractive for a parent to purchase for their child

```html
<!DOCTYPE html>
<html lang="en">
<head>
<meta charset="utf-8">
<title>Floaty Pops! bubble solution labels</title>
<link rel="stylesheet" href="https://fonts.googleapis.com/css2?family=Comic+Neue:wght@400;700&display=swap">
<style>
  :root {
    --board: #2b2b2b;
    --band-red: #e4202a;
    --band-green: #3aa64a;
    --name-red: #e8262b;
    --name-green: #2fae4a;
    --ink: #1c1c1c;
    --paper: #ffffff;
    --volume-yellow: #ffe21a;
    --blue-deep: #1c7fc6;
    --blue-light: #4cb6ea;
    --yellow-deep: #f5b614;
    --yellow-light: #fbe44a;
    --green-deep: #4e9a2c;
    --green-light: #8cc63f;
    --purple-deep: #4a1240;
    --purple-light: #93307f;
  }
  * { box-sizing: border-box; margin: 0; padding: 0; }
  html, body { width: 1200px; height: 752px; overflow: hidden; }
  body {
    background: var(--board);
    font-family: "Comic Neue", "Comic Sans MS", cursive;
    position: relative;
  }
  .label {
    position: absolute;
    width: 492px;
    height: 288px;
    overflow: hidden;
    border-top: 6px solid var(--band-red);
    border-bottom: 6px solid var(--band-red);
  }
  .label--blue   { left: 78px;  top: 62px; }
  .label--yellow { left: 636px; top: 62px; }
  .label--green  { left: 78px;  top: 406px; }
  .label--purple { left: 636px; top: 405px; border-color: var(--band-green); }

  .label__art { position: absolute; inset: 0; }
  .label--blue .label__art   { background: linear-gradient(150deg, var(--blue-deep) 0%, var(--blue-light) 55%, var(--blue-deep) 100%); }
  .label--yellow .label__art { background: radial-gradient(circle at 55% 50%, var(--yellow-light) 0%, var(--yellow-deep) 85%); }
  .label--green .label__art  { background: radial-gradient(circle at 60% 45%, var(--green-light) 0%, var(--green-deep) 90%); }
  .label--purple .label__art { background: radial-gradient(circle at 55% 45%, var(--purple-light) 0%, var(--purple-deep) 90%); }

  .label__name {
    position: absolute;
    left: 26px;
    top: 58px;
    font-size: 56px;
    line-height: 0.95;
    font-weight: 700;
    color: var(--name-red);
  }
  .label--purple .label__name { color: var(--name-green); }

  .label__claims {
    position: absolute;
    left: 44px;
    top: 200px;
    font-size: 22px;
    font-weight: 700;
    color: var(--ink);
    transform: rotate(-12deg);
    transform-origin: left center;
    white-space: nowrap;
  }

  .label__warning {
    position: absolute;
    left: 332px;
    top: 20px;
    width: 148px;
    color: var(--ink);
  }
  .label--blue .label__warning,
  .label--purple .label__warning { color: var(--paper); }
  .warning__title { font-size: 17px; font-weight: 700; margin-bottom: 4px; }
  .warning__text { font-size: 12px; line-height: 15px; font-weight: 400; }

  .label__volume {
    position: absolute;
    left: 220px;
    bottom: 10px;
    font-size: 13px;
    font-weight: 700;
    color: var(--ink);
  }
  .label--blue .label__volume { color: var(--volume-yellow); }
  .label--purple .label__volume { color: var(--paper); }
</style>
</head>
<body>

<section class="label label--blue">
  <div class="label__art" role="img" aria-label="Blue background with floating soap bubbles and sparkles"></div>
  <h2 class="label__name">Floaty<br>Pops!</h2>
  <p class="label__claims">No Dyes | Non Toxic</p>
  <div class="label__warning">
    <h3 class="warning__title">Warning</h3>
    <p class="warning__text">Do not drink bubble solution. If swallowed drink lots of water. Bubble solution is not intended for human or animal consumption. If it comes in contact with your eyes, rinse immediately with water</p>
  </div>
  <p class="label__volume">1oz 473ml</p>
</section>

<section class="label label--yellow">
  <div class="label__art" role="img" aria-label="Yellow background with floating soap bubbles and sparkles"></div>
  <h2 class="label__name">Floaty<br>Pops!</h2>
  <p class="label__claims">No Dyes | Non Toxic</p>
  <div class="label__warning">
    <h3 class="warning__title">Warning</h3>
    <p class="warning__text">Do not drink bubble solution. If swallowed drink lots of water. Bubble solution is not intended for human or animal consumption. If it comes in contact with your eyes, rinse immediately with water</p>
  </div>
  <p class="label__volume">1oz 473ml</p>
</section>

<section class="label label--green">
  <div class="label__art" role="img" aria-label="Green background with floating soap bubbles and sparkles"></div>
  <h2 class="label__name">Floaty<br>Pops!</h2>
  <p class="label__claims">No Dyes | Non Toxic</p>
  <div class="label__warning">
    <h3 class="warning__title">Warning</h3>
    <p class="warning__text">Do not drink bubble solution. If swallowed drink lots of water. Bubble solution is not intended for human or animal consumption. If it comes in contact with your eyes, rinse immediately with water</p>
  </div>
  <p class="label__volume">1oz 473ml</p>
</section>

<section class="label label--purple">
  <div class="label__art" role="img" aria-label="Purple background with floating soap bubbles and sparkles"></div>
  <h2 class="label__name">Floaty<br>Pops!</h2>
  <p class="label__claims">No Dyes | Non Toxic</p>
  <div class="label__warning">
    <h3 class="warning__title">Warning</h3>
    <p class="warning__text">Do not drink bubble solution. If swallowed drink lots of water. Bubble solution is not intended for human or animal consumption. If it comes in contact with your eyes, rinse immediately with water</p>
  </div>
  <p class="label__volume">1oz 473ml</p>
</section>

</body>
</html>
```